Wine Label for a Prosecco Wine Called Vuro

Prosecco is a white sparkling wine from Italy. We are looking for an eye catching, elegant label for this prosecco that is called "Vuro" because it is a young, fresh, lively white sparkling wine. (We do not want to see children or babies featured on the label-- just the name VURO please.) Attached is the old label for your reference, and the bottle type that will be used , which is a dark green Burgundy style bottle (pls ignore the label on the bottle). Please no grapes or wine glasses on the label. We are looking for something: eye catching / fun / ELEGANT (not cheap). We would be happy with a fun color too. Remember-- elegant, eye catching! Thanks!
Updates

Hi All, I think I made a mistake in my brief and have updated it. I also uploaded a competitor's label that we like very much to give better direction to what we are looking for. Also, the word Vuro cannot be vertical, nor can it be broken. It needs to read: VURO or Vuro. Thanks

Target Market(s)

American adults male and female.

Colors
abd036
33a6d7
33b8a4
ffcf3e

Requirements
Must have
• The mandatory information as shown on old labels. The word VURO should be very prominent.
Nice to have
• The uploaded photo of a competitor's prosecco shows a label we really like... if you could play around with this shape and style we'd be very happy.
Should not have
• No grape images, no wine glass images, no images of babies or children.

```html
<!DOCTYPE html>
<html lang="en">
<head>
<meta charset="utf-8">
<title>Vuro Prosecco – Label</title>
<link href="https://fonts.googleapis.com/css2?family=Cinzel:wght@700&family=Josefin+Sans:wght@600;700&family=Open+Sans:wght@400&display=swap" rel="stylesheet">
<style>
  :root {
    --page: #f7f8fa;
    --paper: #ffffff;
    --forest: #1f4d24;
    --ink-green: #1d5a29;
    --leaf-light: #c9e26a;
    --leaf-mid: #8cc63f;
    --leaf-deep: #2a8a45;
  }
  html, body {
    margin: 0;
    padding: 0;
    width: 753px;
    height: 1200px;
    overflow: hidden;
    background: var(--page);
  }
  .canvas {
    position: relative;
    width: 753px;
    height: 1200px;
  }
  .label {
    position: absolute;
    left: 76px;
    top: 220px;
    width: 600px;
    height: 760px;
    background: var(--paper);
  }
  .label__pattern {
    position: absolute;
    left: 0;
    top: 0;
    width: 600px;
    height: 290px;
    background:
      radial-gradient(ellipse at 30% 40%, var(--leaf-light) 0%, transparent 55%),
      radial-gradient(ellipse at 75% 30%, var(--leaf-deep) 0%, transparent 60%),
      linear-gradient(135deg, var(--leaf-mid), var(--leaf-deep) 60%, var(--leaf-mid));
  }
  .label__band {
    position: absolute;
    left: 0;
    top: 288px;
    width: 600px;
    height: 30px;
    background: var(--forest);
  }
  .label__badge {
    position: absolute;
    left: 169px;
    top: 157px;
    width: 233px;
    height: 240px;
    background: var(--forest);
    border: 11px solid var(--paper);
    display: flex;
    align-items: center;
    justify-content: center;
  }
  .label__name {
    font-family: "Josefin Sans", sans-serif;
    font-weight: 700;
    font-size: 64px;
    letter-spacing: 6px;
    color: var(--paper);
    margin-top: 14px;
  }
  .label__wine {
    position: absolute;
    left: 0;
    width: 600px;
    top: 470px;
    text-align: center;
    font-family: "Cinzel", serif;
    font-weight: 700;
    font-size: 82px;
    line-height: 1;
    color: var(--ink-green);
  }
  .label__appellation {
    position: absolute;
    left: 0;
    width: 600px;
    top: 590px;
    text-align: center;
    font-family: "Josefin Sans", sans-serif;
    font-weight: 600;
    font-size: 20px;
    letter-spacing: 1px;
    color: var(--ink-green);
  }
  .label__style {
    position: absolute;
    left: 0;
    width: 600px;
    top: 656px;
    text-align: center;
    font-family: "Open Sans", sans-serif;
    font-weight: 400;
    font-size: 15px;
    color: var(--ink-green);
  }
</style>
</head>
<body>
  <main class="canvas">
    <section class="label">
      <div class="label__pattern" role="img" aria-label="Decorative pattern of swirling green teardrop shapes in light, mid and deep greens"></div>
      <div class="label__band"></div>
      <div class="label__badge">
        <span class="label__name">VURO</span>
      </div>
      <h1 class="label__wine">PROSECCO</h1>
      <p class="label__appellation">DENOMINAZIONE DI ORIGINE CONTROLLATA</p>
      <p class="label__style">FRIZZANTE</p>
    </section>
  </main>
</body>
</html>
```